Bref créative
Business cards, stationery, powerpoint template, and email signature for business consulting firm
Bellwether Advisory Group The Ground Level Method
Simple
Corwin Pike
Consultant
PO Box 7086
Austell, GA 30497
cpike@bellwethgrp.net
We will be adding new employees so I would like the business card file to be changeable. I would like to see both one sided and two-sided business cards.
The logo files will have all parts of the logo available both separate and complete.
This is the complete logo
This is the file with the logo components

```html
<!DOCTYPE html>
<html lang="en">
<head>
<meta charset="utf-8">
<title>Bellwether Advisory Group — Business Card</title>
<link href="https://fonts.googleapis.com/css2?family=Cinzel:wght@400;600&display=swap" rel="stylesheet">
<style>
  :root {
    --page-bg: #e6e4e0;
    --card-white: #ffffff;
    --card-black: #0b0b0b;
    --brand-green: #3e9a3a;
    --brand-green-dark: #2f7d2c;
    --ink-dark: #1f2a3a;
    --ink-grey: #5b5b5b;
    --ink-light: #f2f2f2;
  }
  * { margin: 0; padding: 0; box-sizing: border-box; }
  html, body {
    width: 1200px; height: 900px; overflow: hidden;
    background: var(--page-bg);
    font-family: "Cinzel", "Times New Roman", serif;
  }
  .business-card {
    position: absolute; left: 100px; top: 164px;
    width: 1000px; height: 572px;
    background: var(--card-black);
    overflow: hidden;
    box-shadow: 0 10px 30px rgba(0,0,0,0.25);
  }
  .card-top {
    position: absolute; left: 0; top: 0; width: 100%; height: 276px;
    background: var(--card-white);
  }
  .green-rule {
    position: absolute; left: 0; top: 276px; width: 100%; height: 10px;
    background: var(--brand-green);
  }
  .name-tab {
    position: absolute; right: 0; top: 236px;
    width: 372px; height: 104px;
    background: linear-gradient(var(--brand-green), var(--brand-green-dark));
    border-radius: 14px 0 0 14px;
    padding: 22px 0 0 40px;
    color: var(--ink-light);
  }
  .name-tab .person-name { font-size: 30px; font-weight: 400; letter-spacing: 1px; }
  .name-tab .person-role { font-size: 17px; margin-top: 6px; letter-spacing: 1px; }
  .brand {
    position: absolute; left: 70px; top: 96px;
    display: flex; align-items: center; gap: 22px;
  }
  .brand-mark {
    width: 86px; height: 86px; border-radius: 50%;
    background: var(--brand-green); flex-shrink: 0;
  }
  .brand-name {
    font-size: 32px; font-weight: 600; color: var(--ink-dark);
    letter-spacing: 1px; line-height: 1.1;
  }
  .brand-tagline {
    font-size: 15px; color: var(--ink-grey); letter-spacing: 4px; margin-top: 6px;
  }
  .contact-list {
    position: absolute; left: 50px; top: 400px;
    list-style: none; color: var(--ink-light); font-size: 21px; line-height: 1.3;
  }
  .contact-list li { display: flex; align-items: flex-start; gap: 12px; }
  .contact-list .icon { width: 20px; height: 20px; margin-top: 4px; flex-shrink: 0; }
  .contact-list .indent { padding-left: 32px; }
  .website {
    position: absolute; right: 50px; top: 350px;
    color: var(--ink-light); font-size: 15px; letter-spacing: 7px;
  }
</style>
</head>
<body>
  <div class="business-card">
    <div class="card-top"></div>
    <div class="green-rule"></div>

    <div class="brand">
      <div class="brand-mark"></div>
      <div>
        <div class="brand-name">BELLWETHER ADVISORY GROUP</div>
        <div class="brand-tagline">THE GROUND LEVEL METHOD</div>
      </div>
    </div>

    <div class="name-tab">
      <div class="person-name">Corwin Pike</div>
      <div class="person-role">Consultant</div>
    </div>

    <div class="website">www.bellwethgrp.net</div>

    <ul class="contact-list">
      <li>
        <svg class="icon" viewBox="0 0 20 20"><circle cx="10" cy="10" r="10" fill="#f2f2f2"/><path d="M10 4a4 4 0 0 0-4 4c0 3 4 8 4 8s4-5 4-8a4 4 0 0 0-4-4z" fill="#0b0b0b"/><circle cx="10" cy="8" r="1.5" fill="#f2f2f2"/></svg>
        <span>PO Box 7086 Austell,</span>
      </li>
      <li class="indent">GA 30497</li>
      <li>
        <svg class="icon" viewBox="0 0 20 20"><circle cx="10" cy="10" r="10" fill="#f2f2f2"/><path d="M6.5 5l2 0 1 3-1.3 1a6 6 0 0 0 3 3l1-1.3 3 1v2a1.5 1.5 0 0 1-1.5 1.5A8.5 8.5 0 0 1 5 6.5 1.5 1.5 0 0 1 6.5 5z" fill="#0b0b0b"/></svg>
        <span>404-555-0187</span>
      </li>
      <li>
        <svg class="icon" viewBox="0 0 20 20"><circle cx="10" cy="10" r="10" fill="#f2f2f2"/><rect x="5" y="6.5" width="10" height="7" fill="#0b0b0b"/><path d="M5 6.5l5 4 5-4" fill="none" stroke="#f2f2f2" stroke-width="1"/></svg>
        <span>cpike@bellwethgrp.net</span>
      </li>
      <li>
        <svg class="icon" viewBox="0 0 20 20"><circle cx="10" cy="10" r="10" fill="#f2f2f2"/><circle cx="10" cy="10" r="5.5" fill="none" stroke="#0b0b0b" stroke-width="1.3"/><ellipse cx="10" cy="10" rx="2.3" ry="5.5" fill="none" stroke="#0b0b0b" stroke-width="1.1"/><line x1="4.5" y1="10" x2="15.5" y2="10" stroke="#0b0b0b" stroke-width="1.1"/></svg>
        <span>www.bellwethgrp.net</span>
      </li>
    </ul>
  </div>
</body>
</html>
```